1 postcard flyer for Car Camcorder 2sided FULL COLOR$$$$$$$$

3.5x5.5 inches front and back Full Color
side1 (1 solid color background, portrait layout)
(on the top heading Bold/Stands out) ACCIDENT PROTECTION (Below this on the left side)
Staged Accidents
Crash for Cash
Accident Blames (these three are bad, evil, monstrous things)
(on the right side, a warrior is Standing tall wiith a strong body, instead of a head of man, use a camera lens as head, holding a sword and Shield)(The Shield will have these words written on it and make sure these words are easy to read) Car Camcorder will Protect You from scams

(at the bottom of side1 the footer)
Car Camcorder is your Witness & DOESN'T LIE!

(if anyone has a better design idea to relate the message on the flyer about Car Camcorder will Protect You from scams, please go ahead make your own with the same message that car camcorder will protect you from scams like staged accidents, crash for cash, accident blames)(side1 must be 1 solid color background, portrait layout)

Side2 (whatever solid or multiple color background design of your choice is fine)( a fine looking girl featuring the Car Camcorder functions, the girl picture DOES NOT need to be sexy or showing cleavage, just attractive is good)
What is a Car Camcorder?
Records Video While Driving
Continuous Loop Recording
Easy Installation as a GPS
Auto-On&Off by Cigarette Plug
Impact Detected, Video Clip Will Lock
Car Camcorder will provide You Peace of Mind
(side 2 please leave room for me to stick a 1 inch height label at the bottom)
(also somewhere on this side please add a round or square dot "Starting $60, so reader will know how much car camcorder will cost. I don't want to put any pictures of my car camcorder on the flyer.)

Target Market(s)

Everyone that drives a Vehicle.

Industry/Entity Type

Camera

Requirements
Must have
• Please following the provided template and make sure the design is set per template's instructions. Both sides must be design with 350dpi and CMYK.

```html
<!DOCTYPE html>
<html lang="en">
<head>
<meta charset="utf-8">
<title>What is a Car Camcorder? – Postcard Flyer</title>
<link href="https://fonts.googleapis.com/css2?family=Righteous&display=swap" rel="stylesheet">
<style>
  :root {
    --page-bg: #6f6f6f;
    --flyer-red: #c23b22;
    --flyer-red-deep: #a82f1a;
    --flyer-yellow: #fddc74;
    --feature-red: #c0341d;
    --ink-dark: #26221f;
    --gold-light: #f8dc86;
    --gold-dark: #c0812b;
    --title-shadow: #5a1e0e;
    --badge-light: #8b5a44;
    --badge-dark: #5a3323;
    --badge-text: #f6e7cf;
    --photo-light: #e9d3b4;
    --photo-dark: #8a5a3c;
  }
  * { margin: 0; padding: 0; box-sizing: border-box; }
  html, body {
    width: 1200px; height: 900px; overflow: hidden;
    background: var(--page-bg);
  }
  .flyer {
    position: absolute; left: 90px; top: 120px;
    width: 1020px; height: 660px;
    background: var(--flyer-red);
    overflow: hidden;
    font-family: "Righteous", sans-serif;
  }
  .flyer__panel { position: absolute; inset: 0; }
  .flyer__title {
    position: absolute; left: 248px; top: 52px;
    font-size: 56px; line-height: 1; font-weight: 400;
    background: linear-gradient(to bottom, var(--gold-light) 20%, var(--gold-dark) 95%);
    -webkit-background-clip: text; background-clip: text;
    color: transparent;
    -webkit-text-stroke: 1.2px var(--title-shadow);
    filter: drop-shadow(2px 3px 0 var(--title-shadow));
    white-space: nowrap;
  }
  .flyer__photo {
    position: absolute; left: 38px; top: 30px;
    width: 190px; height: 630px;
    border-radius: 95px 95px 0 0;
    background: linear-gradient(to bottom, var(--photo-light) 0%, var(--photo-light) 50%, var(--photo-dark) 66%, var(--photo-dark) 100%);
  }
  .features { list-style: none; }
  .features__item {
    position: absolute; left: 355px;
    display: flex; align-items: center; gap: 15px;
    height: 38px;
    font-size: 28px; color: var(--feature-red); white-space: nowrap;
  }
  .features__item--1 { top: 241px; }
  .features__item--2 { top: 301px; }
  .features__item--3 { top: 361px; }
  .features__item--4 { top: 414px; }
  .features__item--5 { top: 471px; }
  .features__tick { width: 40px; height: 38px; flex: none; }
  .flyer__tagline {
    position: absolute; left: 293px; top: 529px;
    font-size: 31px; line-height: 38px; color: var(--ink-dark); white-space: nowrap;
  }
  .price-badge {
    position: absolute; left: 813px; top: 247px;
    width: 190px; height: 190px;
  }
  .price-badge svg { display: block; }
  .price-badge__text {
    position: absolute; inset: 0;
    display: flex; flex-direction: column; align-items: center; justify-content: center;
    color: var(--badge-text);
    -webkit-text-stroke: 1px var(--badge-dark);
    text-shadow: 2px 2px 0 #2e160c;
    line-height: 1.05;
  }
  .price-badge__label { font-size: 32px; }
  .price-badge__amount { font-size: 44px; }
</style>
</head>
<body>
  <section class="flyer">
    <svg class="flyer__panel" width="1020" height="660" viewBox="0 0 1020 660" aria-hidden="true">
      <path d="M0,170 C110,150 200,260 215,660 L0,660 Z" fill="var(--flyer-red-deep)"/>
      <path d="M265,175 L1020,175 L1020,660 L212,660 C240,520 245,330 265,175 Z" fill="var(--flyer-yellow)"/>
    </svg>

    <div class="flyer__photo" role="img" aria-label="Photo of a smiling young woman presenting the camcorder features with open hands"></div>

    <h1 class="flyer__title">What is a Car Camcorder?</h1>

    <ul class="features">
      <li class="features__item features__item--1">
        <svg class="features__tick" viewBox="0 0 40 38" aria-hidden="true"><rect x="2" y="10" width="26" height="26" fill="none" stroke="var(--feature-red)" stroke-width="3"/><path d="M8,22 L15,30 L37,3" fill="none" stroke="var(--feature-red)" stroke-width="5" stroke-linecap="round" stroke-linejoin="round"/></svg>
        Records Video While Driving
      </li>
      <li class="features__item features__item--2">
        <svg class="features__tick" viewBox="0 0 40 38" aria-hidden="true"><rect x="2" y="10" width="26" height="26" fill="none" stroke="var(--feature-red)" stroke-width="3"/><path d="M8,22 L15,30 L37,3" fill="none" stroke="var(--feature-red)" stroke-width="5" stroke-linecap="round" stroke-linejoin="round"/></svg>
        Continuous Loop Recording
      </li>
      <li class="features__item features__item--3">
        <svg class="features__tick" viewBox="0 0 40 38" aria-hidden="true"><rect x="2" y="10" width="26" height="26" fill="none" stroke="var(--feature-red)" stroke-width="3"/><path d="M8,22 L15,30 L37,3" fill="none" stroke="var(--feature-red)" stroke-width="5" stroke-linecap="round" stroke-linejoin="round"/></svg>
        Easy Installation as a GPS
      </li>
      <li class="features__item features__item--4">
        <svg class="features__tick" viewBox="0 0 40 38" aria-hidden="true"><rect x="2" y="10" width="26" height="26" fill="none" stroke="var(--feature-red)" stroke-width="3"/><path d="M8,22 L15,30 L37,3" fill="none" stroke="var(--feature-red)" stroke-width="5" stroke-linecap="round" stroke-linejoin="round"/></svg>
        Auto-On&amp;Off by Cigarette Plug
      </li>
      <li class="features__item features__item--5">
        <svg class="features__tick" viewBox="0 0 40 38" aria-hidden="true"><rect x="2" y="10" width="26" height="26" fill="none" stroke="var(--feature-red)" stroke-width="3"/><path d="M8,22 L15,30 L37,3" fill="none" stroke="var(--feature-red)" stroke-width="5" stroke-linecap="round" stroke-linejoin="round"/></svg>
        Impact Detected, Video Clip Will Lock
      </li>
    </ul>

    <p class="flyer__tagline">Car Camcorder will provide You Peace of Mind</p>

    <div class="price-badge">
      <svg width="190" height="190" viewBox="0 0 190 190" aria-hidden="true">
        <defs>
          <radialGradient id="badgeFill" cx="45%" cy="35%" r="70%">
            <stop offset="0" stop-color="var(--badge-light)"/>
            <stop offset="1" stop-color="var(--badge-dark)"/>
          </radialGradient>
        </defs>
        <circle cx="95" cy="95" r="94" fill="url(#badgeFill)"/>
        <circle cx="95" cy="95" r="84" fill="none" stroke="var(--badge-text)" stroke-width="5" stroke-dasharray="1.5 3" opacity="0.75"/>
      </svg>
      <div class="price-badge__text">
        <span class="price-badge__label">Starting</span>
        <span class="price-badge__amount">$60</span>
      </div>
    </div>
  </section>
</body>
</html>
```